ZAMO needs a beautiful/corp web page

We are a pump an compressor repair facility in Alberta Canada. We love clean looks. white yellows greens blues. main page should involve conola fields, sun shine

Reason: i will be guaranteeing the project keep up the good work

Requirements
Must have
• open conola fields

```html
<!DOCTYPE html>
<html lang="en">
<head>
<meta charset="utf-8">
<title>ZAMO — Pump &amp; Compressor Repair</title>
<link rel="stylesheet" href="https://fonts.googleapis.com/css2?family=Didact+Gothic&family=Open+Sans:wght@400;600;700&display=swap">
<style>
  :root {
    --accent-yellow: #f3b834;
    --icon-orange: #ffb400;
    --icon-green: #a5cf1f;
    --band-blue: #0f8db3;
    --band-green: #a7d11f;
    --hero-top: #e8e2a0;
    --hero-bottom: #dccf4e;
    --ink: #2a2a2a;
    --headline-ink: #2e2e2e;
    --nav-ink: #3a3a3a;
    --muted: #6b6b6b;
    --top-dark: #2b2b33;
    --white: #ffffff;
  }
  * { box-sizing: border-box; margin: 0; padding: 0; }
  html, body { width: 1200px; height: 979px; overflow: hidden; background: var(--white); }
  body { position: relative; font-family: "Open Sans", sans-serif; }

  .hero {
    position: absolute; left: 0; top: 0; width: 1200px; height: 547px;
    background: linear-gradient(180deg, var(--hero-top) 0%, var(--hero-bottom) 100%);
  }

  .top-rule { position: absolute; left: 0; top: 0; width: 1200px; height: 4px; background: var(--accent-yellow); z-index: 3; }
  .top-rule span { position: absolute; left: 76px; width: 262px; height: 4px; background: var(--top-dark); }

  .site-header {
    position: absolute; left: 0; top: 4px; width: 1200px; height: 86px;
    background: rgba(255,255,255,0.86); z-index: 2;
    box-shadow: 0 1px 3px rgba(0,0,0,0.15);
  }
  .brand { position: absolute; left: 104px; top: 26px; display: flex; align-items: center; gap: 10px; }
  .brand-dot { width: 26px; height: 26px; border-radius: 50%; background: var(--accent-yellow); }
  .brand-name { font-family: "Open Sans", sans-serif; font-weight: 700; font-size: 30px; letter-spacing: 1px; color: var(--ink); }

  .main-nav { position: absolute; top: 0; left: 0; height: 86px; width: 1200px; }
  .main-nav a {
    position: absolute; top: 0; height: 86px; line-height: 86px;
    font-family: "Didact Gothic", sans-serif; font-size: 12.5px; letter-spacing: 1.2px;
    color: var(--nav-ink); text-decoration: none; transform: translateX(-50%); white-space: nowrap;
  }
  .main-nav a.is-active { background: var(--accent-yellow); width: 66px; text-align: center; color: #222; }
  .nav-divider { position: absolute; left: 1068px; top: 36px; width: 1px; height: 24px; background: #c8c8c8; }
  .search-btn { position: absolute; left: 1089px; top: 33px; width: 26px; height: 26px; background: var(--accent-yellow); }

  .headline { position: absolute; left: 93px; top: 270px; z-index: 1; font-weight: 400; }
  .headline span {
    display: block; width: max-content; margin-bottom: 4px;
    background: rgba(255,255,255,0.45);
    font-family: "Didact Gothic", sans-serif; font-size: 40px; letter-spacing: 6.4px;
    color: var(--headline-ink); padding: 6px 18px 6px 17px; line-height: 51px;
  }

  .info-band { position: absolute; left: 0; top: 547px; width: 1200px; height: 44px; display: flex; }
  .info-band .label {
    width: 338px; background: var(--band-blue); color: var(--white);
    font-weight: 600; font-size: 18px; letter-spacing: 0.6px; padding-left: 112px; line-height: 44px; white-space: nowrap;
  }
  .info-band .text {
    flex: 1; background: var(--band-green); color: var(--white);
    font-weight: 600; font-size: 15.5px; letter-spacing: 0.6px; padding-left: 39px; line-height: 44px; white-space: nowrap;
  }

  .features { position: absolute; left: 0; top: 685px; width: 1200px; }
  .feature { position: absolute; width: 230px; transform: translateX(-50%); text-align: center; }
  .feature-icon { width: 109px; height: 109px; border-radius: 50%; margin: 0 auto; display: flex; align-items: center; justify-content: center; }
  .feature-icon.orange { background: var(--icon-orange); }
  .feature-icon.green { background: var(--icon-green); }
  .feature-title { font-family: "Didact Gothic", sans-serif; font-size: 17px; letter-spacing: 1.5px; margin-top: 7px; }
  .feature-title.orange { color: var(--icon-orange); }
  .feature-title.green { color: var(--icon-green); }
  .feature-text { font-family: Verdana, "Open Sans", sans-serif; font-size: 11px; line-height: 13px; color: var(--muted); margin-top: 18px; }
</style>
</head>
<body>
  <div class="hero" role="img" aria-label="Photograph of an open yellow canola field in bloom under a sunny blue sky with white clouds"></div>

  <div class="top-rule"><span></span></div>

  <header class="site-header">
    <div class="brand"><span class="brand-dot"></span><span class="brand-name">ZAMO</span></div>
    <nav class="main-nav">
      <a class="is-active" href="#" style="left:652px">HOME</a>
      <a href="#" style="left:743px">SOLUTIONS</a>
      <a href="#" style="left:843px">PRODUCTS</a>
      <a href="#" style="left:934px">ABOUT</a>
      <a href="#" style="left:1021px">CONTACT</a>
    </nav>
    <span class="nav-divider"></span>
    <span class="search-btn">
      <svg width="26" height="26" viewBox="0 0 26 26"><circle cx="11" cy="11" r="5" fill="none" stroke="#fff" stroke-width="2.2"/><line x1="14.5" y1="14.5" x2="20" y2="20" stroke="#fff" stroke-width="2.8" stroke-linecap="round"/></svg>
    </span>
  </header>

  <h1 class="headline">
    <span>We are a pump an compressor</span>
    <span>repair facility in Alberta Canada</span>
  </h1>

  <div class="info-band">
    <div class="label">LOREM IPSUM DOLOR</div>
    <div class="text">Lorem ipsum dolor sit amet, consectetur adipisicing elit, sed do eiusmod tempor.</div>
  </div>

  <svg width="0" height="0" style="position:absolute">
    <defs>
      <marker id="arrow-head" viewBox="0 0 10 10" refX="5" refY="5" markerWidth="3" markerHeight="3" orient="auto">
        <path d="M0 0 L10 5 L0 10 Z" fill="#fff"/>
      </marker>
    </defs>
  </svg>

  <section class="features">
    <div class="feature" style="left:208px">
      <div class="feature-icon orange">
        <svg width="62" height="62" viewBox="0 0 62 62" fill="none" stroke="#fff" stroke-width="6" stroke-linecap="butt">
          <path d="M12 44 L25 20" marker-end="url(#arrow-head)"/>
          <path d="M37 14 L47 32" marker-end="url(#arrow-head)"/>
          <path d="M46 50 L22 50" marker-end="url(#arrow-head)"/>
        </svg>
      </div>
      <div class="feature-title orange">LOREM IPSUM</div>
      <p class="feature-text">Sed ut perspiciatis unde omnis iste natus error sit voluptatem accusantium dolor-emque laudantium</p>
    </div>
    <div class="feature" style="left:470px">
      <div class="feature-icon green">
        <svg width="62" height="62" viewBox="0 0 62 62" fill="none" stroke="#fff" stroke-width="3">
          <circle cx="31" cy="31" r="27"/><ellipse cx="31" cy="31" rx="12" ry="27"/><line x1="31" y1="4" x2="31" y2="58"/><line x1="4" y1="31" x2="58" y2="31"/><path d="M8 18 H54 M8 44 H54"/>
        </svg>
      </div>
      <div class="feature-title green">LOREM IPSUM</div>
      <p class="feature-text">Sed ut perspiciatis unde omnis iste natus error sit voluptatem accusantium dolor-emque laudantium</p>
    </div>
    <div class="feature" style="left:731px">
      <div class="feature-icon orange">
        <svg width="62" height="62" viewBox="0 0 62 62" fill="none" stroke="#fff" stroke-width="6" stroke-linecap="butt">
          <path d="M12 44 L25 20" marker-end="url(#arrow-head)"/>
          <path d="M37 14 L47 32" marker-end="url(#arrow-head)"/>
          <path d="M46 50 L22 50" marker-end="url(#arrow-head)"/>
        </svg>
      </div>
      <div class="feature-title orange">LOREM IPSUM</div>
      <p class="feature-text">Sed ut perspiciatis unde omnis iste natus error sit voluptatem accusantium dolor-emque laudantium</p>
    </div>
    <div class="feature" style="left:993px">
      <div class="feature-icon green">
        <svg width="62" height="62" viewBox="0 0 62 62" fill="none" stroke="#fff" stroke-width="3">
          <circle cx="31" cy="31" r="27"/><ellipse cx="31" cy="31" rx="12" ry="27"/><line x1="31" y1="4" x2="31" y2="58"/><line x1="4" y1="31" x2="58" y2="31"/><path d="M8 18 H54 M8 44 H54"/>
        </svg>
      </div>
      <div class="feature-title green">LOREM IPSUM</div>
      <p class="feature-text">Sed ut perspiciatis unde omnis iste natus error sit voluptatem accusantium dolor-emque laudantium</p>
    </div>
  </section>
</body>
</html>
```